Design a corporate looking website for Harbourline Funding

Need design only WordPress mock up for Harbourline Funding who provides short term finance solutions to other businesses. We need a corporate looking website that depicts a trustworthy, Dynamic fast acting company.
Visit http://q7.pagemockery.net/ for current mock up We need something like e this but not the same with a design that depicts corporate with more colour and images, needs to install trust and fast action. Please feel free to change the layout as I am not wedded to current design but am happy with what on the landing page.

Target Market(s)

Small to medium sized Businesses

Industry/Entity Type

Finance

Number of Pages Required

1 page

Font styles to use
Sans Serif

Requirements
Must have
• Design Landing pages in WordPress
• Visit http://q7.pagemockery.net/ for current mock up need Layout like this but with a design that depicts corporate with more colour and images, needs to install trust and fast action. Please feel free to change the layout as I am not happy with current design but am wedded to what on the landing page.
Should not have
• any copyright material on it.

```html
<!DOCTYPE html>
<html lang="en">
<head>
<meta charset="utf-8">
<title>Harbourline Funding – Commission Assistance</title>
<link rel="stylesheet" href="https://fonts.googleapis.com/css2?family=Raleway:wght@400;500;600;700&family=Lato:ital,wght@0,400;0,700;1,400&display=swap">
<style>
:root{
  --blue:#3f82c4;
  --blue-dark:#2a5f97;
  --red:#d9213f;
  --ink:#2b2b2b;
  --muted:#6b6b6b;
  --band:#ebebeb;
  --line:#cfcfcf;
  --footer:#2f2f2f;
  --footer-base:#232323;
  --footer-text:#bdbdbd;
  --white:#ffffff;
}
*{box-sizing:border-box;margin:0;padding:0}
html,body{width:1200px;height:3448px;overflow:hidden}
body{font-family:"Lato",sans-serif;color:var(--ink);background:var(--white);position:relative}
h1,h2,h3,h4,.raleway{font-family:"Raleway",sans-serif;font-weight:500}
.abs{position:absolute}

/* header */
.site-header{position:absolute;top:0;left:0;width:1200px;height:110px;border-bottom:1px solid #eee;display:flex;align-items:center;padding:0 32px}
.brand{display:flex;align-items:center;gap:14px}
.brand-dot{width:34px;height:34px;border-radius:50%;background:var(--blue)}
.brand-name{font-family:"Raleway",sans-serif;font-weight:700;font-size:27px;color:var(--blue-dark)}
.main-nav{margin-left:auto;display:flex;gap:52px;font-family:"Raleway",sans-serif;font-size:13px;font-weight:500;text-transform:uppercase;color:#333}

/* hero */
.hero-title{left:32px;top:160px;font-size:42px;letter-spacing:1px;text-transform:uppercase;color:#222}
.hero-sub{left:32px;top:224px;font-size:34px;font-weight:400;line-height:42px;color:#444}
.hero-copy{left:32px;width:520px;font-size:22px;line-height:32px;color:#777;font-family:"Raleway",sans-serif}
.btn{display:flex;align-items:center;justify-content:center;font-family:"Raleway",sans-serif;font-weight:700;text-transform:uppercase;color:var(--white)}
.btn-red{background:var(--red)}
.link-more{left:368px;top:572px;font-family:"Raleway",sans-serif;font-weight:700;font-size:16px;color:var(--blue-dark);letter-spacing:1px}
.monitor{left:612px;top:158px;width:560px}
.monitor-body{background:#1d1d1d;border-radius:12px 12px 0 0;padding:14px 14px 0}
.video{height:326px;background:linear-gradient(135deg,#8a4a3c,#c7a07a 45%,#4f5f78);display:flex;align-items:center;justify-content:center}
.video-caption{height:48px;background:#c9c9c9;font-family:"Raleway",sans-serif;font-size:28px;color:#555;display:flex;align-items:center;justify-content:center}

/* steps */
.steps-band{left:0;top:685px;width:1200px;height:538px;background:var(--band)}
.section-title{width:1200px;left:0;text-align:center;text-transform:uppercase;color:#333}
.step-label{position:absolute;color:var(--white);font-family:"Raleway",sans-serif;text-align:center}
.cta-strip{left:32px;top:1097px;width:1140px;height:74px}

/* reviews & faq */
.col-head{font-size:24px;text-transform:uppercase;color:#222}
.review{position:absolute;left:32px;display:flex;gap:32px;width:520px}
.avatar{flex:none;width:64px;height:64px;border-radius:50%;background:linear-gradient(#7a8796,#c3b5a8)}
.review p{font-style:italic;font-size:17px;line-height:24px;color:#555}
.review strong{display:block;margin-top:8px;font-size:17px;color:#111}
.faq{position:absolute;left:600px;width:572px}
.faq h4{font-size:21px;color:#333;display:flex;align-items:center;gap:18px}
.faq p{font-size:15px;line-height:26px;color:#555;margin-top:12px}

/* contact */
.form-area{left:32px;top:1970px;width:531px}
.form-area h3{font-size:26px;font-weight:400;color:#222}
.field-label{position:absolute;font-size:12px;text-transform:uppercase;color:#333;letter-spacing:.5px}
.field-label i{color:var(--red);font-style:normal}
.field{position:absolute;border:1px solid var(--line);height:36px;background:#fff}
.map{left:600px;top:1982px;width:572px;height:402px;background:linear-gradient(135deg,#e9e4da,#f1ede4 55%,#e2d9c4)}

/* member */
.member-band{left:0;top:2501px;width:1200px;height:313px;background:#f3f3f3}

/* footer */
.site-footer{left:0;top:2814px;width:1200px;height:496px;background:var(--footer);color:var(--footer-text)}
.footer-base{left:0;top:3310px;width:1200px;height:138px;background:var(--footer-base);color:#8a8a8a;font-size:14px}
.f-head{font-size:16px;letter-spacing:2px;text-transform:uppercase;color:#ddd}
.f-list{list-style:none;font-family:"Raleway",sans-serif;font-size:12.5px;text-transform:uppercase;line-height:31px;color:#ccc}
.f-list li::before{content:"›";margin-right:12px}
.post{border-bottom:1px solid #444;padding-bottom:16px;margin-bottom:18px}
.post b{display:block;font-weight:400;font-size:15px;line-height:21px;color:#e5e5e5}
.post span{font-size:12px;color:#999}
.social{display:flex;gap:12px}
.social span{width:36px;height:36px;background:#555}
</style>
</head>
<body>

<header class="site-header">
  <div class="brand"><span class="brand-dot"></span><span class="brand-name">Harbourline Funding</span></div>
  <nav class="main-nav"><span>Home</span><span>Services</span><span>Why Harbourline</span><span>Investors</span><span>About Us</span><span>Contact Us</span><span>Members Login</span></nav>
</header>

<!-- hero -->
<h1 class="abs hero-title">Commission Assistance</h1>
<h2 class="abs hero-sub">Providing Commission Advances<br>When You Need It</h2>
<p class="abs hero-copy" style="top:332px">Providing immediate commission advance solutions for all industries</p>
<p class="abs hero-copy" style="top:416px">Our background is sales, property and finance. We understand the issues faced with Small to medium Businesses</p>
<a class="abs btn btn-red" style="left:32px;top:563px;width:283px;height:46px;font-size:17px">Get Started Now</a>
<span class="abs link-more">FIND OUT MORE</span>

<div class="abs monitor">
  <div class="monitor-body">
    <div class="video" role="img" aria-label="Video still of a busy city street with billboards">
      <svg width="96" height="96" viewBox="0 0 96 96"><circle cx="48" cy="48" r="44" fill="none" stroke="#fff" stroke-width="7"/><polygon points="38,28 68,48 38,68" fill="#fff"/></svg>
    </div>
    <div class="video-caption" style="margin:0 -14px">Watch Video and Learn More</div>
  </div>
  <svg width="560" height="80" viewBox="0 0 560 80"><rect x="250" y="0" width="60" height="62" fill="#bdbdbd"/><ellipse cx="280" cy="66" rx="80" ry="10" fill="#cfcfcf"/></svg>
</div>

<!-- steps -->
<div class="abs steps-band"></div>
<h2 class="abs section-title" style="top:718px;font-size:38px">3 Easy Steps to a Stress Free Solution</h2>
<svg class="abs" style="left:32px;top:798px" width="1140" height="250" viewBox="0 0 1140 250">
  <polygon points="4,4 336,4 362,110 336,216 4,216" fill="#4a86c2" stroke="#fff" stroke-width="8"/>
  <polygon points="404,4 740,4 766,110 740,216 404,216" fill="#4a86c2" stroke="#fff" stroke-width="8"/>
  <polygon points="802,4 1136,4 1136,216 969,244 802,216" fill="#4a86c2" stroke="#fff" stroke-width="8"/>
</svg>
<div class="step-label" style="left:36px;top:826px;width:330px;font-size:80px;font-weight:400">1</div>
<div class="step-label" style="left:36px;top:952px;width:330px;font-size:38px">Call or click</div>
<div class="step-label" style="left:436px;top:826px;width:330px;font-size:80px;font-weight:400">2</div>
<div class="step-label" style="left:436px;top:952px;width:330px;font-size:38px">Fill out &amp; Sign</div>
<div class="step-label" style="left:836px;top:826px;width:330px;font-size:80px;font-weight:400">3</div>
<div class="step-label" style="left:836px;top:940px;width:330px;font-size:30px;line-height:34px">Funds in bank<br>in 4 hours</div>

<svg class="abs cta-strip" width="1140" height="74" viewBox="0 0 1140 74">
  <rect x="0" y="0" width="820" height="74" fill="#fff"/>
  <polygon points="796,0 1140,0 1110,37 1140,74 796,74 826,37" fill="var(--red)"/>
</svg>
<div class="abs raleway" style="left:70px;top:1110px;font-size:38px;color:var(--blue-dark)">SERIOUSLY, IT CAN’T GET ANY EASIER!</div>
<div class="abs raleway" style="left:880px;top:1108px;font-size:40px;font-weight:700;color:#fff">START NOW!</div>

<!-- reviews -->
<h3 class="abs col-head" style="left:32px;top:1300px">What people say about us</h3>
<div class="review" style="top:1380px"><div class="avatar" role="img" aria-label="Client portrait"></div><div><p>Mauris elit justo, molestie sed purus eu, porttitor rutrum massa. Cras elementum sollicitudin metus</p><strong>CEO Company LTD.</strong></div></div>
<div class="review" style="top:1518px"><div class="avatar" role="img" aria-label="Client portrait"></div><div><p>Mauris elit justo, molestie sed purus eu, porttitor rutrum massa. Cras elementum sollicitudin metus</p><strong>CEO Company LTD.</strong></div></div>
<div class="review" style="top:1656px"><div class="avatar" role="img" aria-label="Client portrait"></div><div><p>Mauris elit justo, molestie sed purus eu, porttitor rutrum massa. Cras elementum sollicitudin metus</p><strong>CEO Company LTD.</strong></div></div>

<!-- faq -->
<h3 class="abs col-head" style="left:602px;top:1300px">Frequently asked questions</h3>
<div class="faq" style="top:1380px"><h4><svg width="24" height="26"><polygon points="2,2 22,13 2,24" fill="none" stroke="#4a86c2" stroke-width="3"/></svg>How long does it take?</h4><p>Please change this to an actual answer. This is just a placeholder text. It can also contain images.</p></div>
<div class="faq" style="top:1500px"><h4><svg width="24" height="26"><polygon points="2,2 22,13 2,24" fill="none" stroke="#4a86c2" stroke-width="3"/></svg>What are the conditions?</h4><p>Please change this to an actual answer. This is just a placeholder text. It can also contain images. Please change this to an actual answer. This is just a.</p></div>
<div class="faq" style="top:1618px"><h4><svg width="24" height="26"><polygon points="2,2 22,13 2,24" fill="none" stroke="#4a86c2" stroke-width="3"/></svg>What documents do I need?</h4><p>Please change this to an actual answer. This is just a placeholder text. It can also contain images. Please change this to an actual answer. This is just a placeholder text. It can also contain images.</p></div>

<!-- contact -->
<h2 class="abs section-title" style="top:1828px;font-size:32px">Get in Touch!</h2>
<p class="abs" style="left:0;width:1200px;text-align:center;top:1890px;font-size:22px;color:#555">Still have questions? Contact us by filling the form below</p>
<div class="abs form-area">
  <h3>Email us</h3>
  <span class="field-label" style="left:0;top:62px">Name <i>*</i></span>
  <span class="field-label" style="left:184px;top:62px">Email <i>*</i></span>
  <span class="field-label" style="left:369px;top:62px">Phone</span>
  <div class="field" style="left:0;top:84px;width:162px"></div>
  <div class="field" style="left:184px;top:84px;width:162px"></div>
  <div class="field" style="left:369px;top:84px;width:162px"></div>
  <span class="field-label" style="left:0;top:154px">Subject <i>*</i></span>
  <span class="field-label" style="left:369px;top:154px">Phone</span>
  <div class="field" style="left:0;top:176px;width:346px"></div>
  <div class="field" style="left:369px;top:176px;width:162px"></div>
  <span class="field-label" style="left:0;top:246px">Message <i>*</i></span>
  <div class="field" style="left:0;top:268px;width:531px;height:150px"></div>
  <a class="btn" style="position:absolute;left:0;top:444px;width:168px;height:53px;background:#2b80c2;font-size:15px">Send Message</a>
</div>
<div class="abs map" role="img" aria-label="Street map showing the office location"></div>

<!-- member -->
<div class="abs member-band"></div>
<h2 class="abs section-title" style="top:2550px;font-size:34px">Become a Harbourline Funding Member Now!</h2>
<p class="abs" style="left:0;width:1200px;text-align:center;top:2606px;font-size:24px;color:#555">Get all membership benefits which include Discounts and more!</p>
<a class="abs btn btn-red" style="left:379px;top:2694px;width:361px;height:60px;font-size:20px">Become a Member Now!</a>

<!-- footer -->
<footer class="abs site-footer">
  <div class="abs brand" style="left:32px;top:76px"><span class="brand-dot" style="width:28px;height:28px;background:#fff"></span><span class="brand-name" style="color:#fff;font-size:22px">Harbourline Funding</span></div>
  <p class="abs" style="left:32px;top:156px;width:260px;font-size:14px;line-height:21px;color:#ddd">Providing immediate commission advance solutions for all industries</p>
  <p class="abs" style="left:32px;top:230px;width:260px;font-size:14px;line-height:21px">Headquarters:<br>48 Quayside Row, Suite 12<br>Portmere, PM 20418<br><br>Phone: (20) 5550 1187<br>Fax: (20) 5550 1190<br>Email: hello@harbourline.example</p>
  <h4 class="abs f-head" style="left:315px;top:86px">Services</h4>
  <ul class="abs f-list" style="left:315px;top:130px">
    <li>Why Harbourline</li><li>Small Business Loans</li><li>Medium Business Loans</li><li>Currency Exchange</li><li>Other Services</li><li>Even More Services</li><li>About Harbourline Funding</li>
  </ul>
  <h4 class="abs f-head" style="left:600px;top:86px">Posts</h4>
  <div class="abs" style="left:600px;top:134px;width:250px">
    <div class="post"><b>Lorem ipsum dolor sit amet, consectetur</b><span>10th July 2014</span></div>
    <div class="post"><b>Elit Assumenda vel amet dolorum quasi</b><span>10th July 2014</span></div>
    <div class="post" style="border:0"><b>Debitis nihil placeat, illum est nisi</b><span>10th July 2014</span></div>
  </div>
  <div class="abs raleway" style="left:885px;top:70px;width:287px;text-align:center;font-size:44px;font-weight:600;color:#fff">18,465</div>
  <div class="abs" style="left:885px;top:134px;width:287px;text-align:center;font-size:13px;letter-spacing:2px">HAPPILY SERVED</div>
  <div class="abs raleway" style="left:885px;top:190px;font-size:21px;color:#e5e5e5">Subscribe to Our Newsletter</div>
  <div class="abs" style="left:885px;top:244px;width:202px;height:34px;background:#3e3e3e;font-size:12px;color:#888;padding:9px 0 0 48px">Enter Your Email</div>
  <svg class="abs" style="left:897px;top:253px" width="18" height="14"><rect x="1" y="1" width="16" height="12" fill="none" stroke="#888"/><polyline points="1,1 9,8 17,1" fill="none" stroke="#888"/></svg>
  <div class="abs btn" style="left:1087px;top:244px;width:85px;height:34px;background:#5b8a8a;font-size:13px;text-transform:none;font-weight:600">Subscribe</div>
  <div class="abs social" style="left:885px;top:306px"><span></span><span></span><span></span><span></span><span></span></div>
</footer>
<div class="abs footer-base">
  <p class="abs" style="left:32px;top:42px;line-height:28px">Copyrights © 2016 Harbourline Funding · All Rights Reserved<br>Terms of Use | Privacy Policy</p>
  <p class="abs" style="right:28px;top:70px">✉ desk@harbourline.example &nbsp; · &nbsp; +20-55-5012-2040</p>
</div>

</body>
</html>
```